Business Card Design Project

KV Strategy Partners is a management consulting business with C-suite (CEO/CFO etc) target clients. Logo selected is blue with simple/serious typefaces.

Target Market(s)

CEOs and CFOs of large corporates

Industry/Entity Type

Management Consulting

Font styles to use
Serif

Colors
3276b5

Requirements
Must have
• Tag line: Shaping enduring partnerships (use different font)
Address: 457 Cedar Brook Lane #03-22 Singapore 519307
Telephone: +65 8372 6094
Email: kvlorne@mailbox47.com

```html
<!DOCTYPE html>
<html lang="en">
<head>
<meta charset="utf-8">
<title>KV Strategy Partners — Business Cards</title>
<link rel="stylesheet" href="https://fonts.googleapis.com/css2?family=Marcellus&family=Marcellus+SC&family=Open+Sans:wght@600&display=swap">
<style>
  :root {
    --bg: #ececec;
    --brand-blue: #1565a5;
    --ink: #1b1b1f;
    --paper: #ffffff;
    --rule-light: rgba(255,255,255,0.55);
    --card-shadow: 0 10px 28px rgba(0,0,0,0.12);
  }
  * { box-sizing: border-box; margin: 0; padding: 0; }
  html, body {
    width: 1200px; height: 1001px; overflow: hidden;
    background: var(--bg);
  }
  .sheet { position: relative; width: 1200px; height: 1001px; }
  .card {
    position: absolute; top: 350px;
    width: 525px; height: 300px;
    box-shadow: var(--card-shadow);
  }

  /* Back side: contact details */
  .card-back { left: 50px; background: var(--brand-blue); }
  .card-back .wordmark {
    position: absolute; left: 40px; top: 78px; width: 190px;
    font-family: "Marcellus SC", serif; font-size: 26px; line-height: 1.15;
    color: var(--ink); letter-spacing: 0.5px;
  }
  .card-back .divider {
    position: absolute; left: 252px; top: 90px;
    width: 1px; height: 150px; background: var(--rule-light);
  }
  .contact-list {
    position: absolute; left: 276px; top: 138px; list-style: none;
    font-family: "Marcellus SC", serif; font-size: 14px; line-height: 1.5;
    color: var(--ink); white-space: nowrap;
  }
  .contact-list li { display: flex; align-items: flex-start; gap: 9px; }
  .contact-list svg { width: 11px; height: 11px; margin-top: 4px; flex: none; fill: var(--paper); }
  .contact-list .icon-spacer { width: 11px; flex: none; }

  /* Front side: name and tagline */
  .card-front { left: 625px; background: var(--paper); }
  .card-front .wordmark {
    position: absolute; left: 0; right: 0; top: 92px; text-align: center;
    font-family: "Marcellus", serif; font-size: 36px;
    color: var(--brand-blue); letter-spacing: 0.5px;
  }
  .card-front .tagline {
    position: absolute; left: 0; right: 0; top: 148px; text-align: center;
    font-family: "Open Sans", sans-serif; font-weight: 600; font-size: 15px;
    color: var(--brand-blue); letter-spacing: 0.3px;
  }
</style>
</head>
<body>
<main class="sheet">
  <section class="card card-back" aria-label="Business card back">
    <div class="wordmark">KV Strategy Partners</div>
    <div class="divider"></div>
    <ul class="contact-list">
      <li>
        <svg viewBox="0 0 12 12" aria-hidden="true"><path d="M6 0a4 4 0 0 0-4 4c0 3 4 8 4 8s4-5 4-8a4 4 0 0 0-4-4zm0 5.5A1.5 1.5 0 1 1 6 2.5a1.5 1.5 0 0 1 0 3z"/></svg>
        <span>457 Cedar Brook Lane</span>
      </li>
      <li><span class="icon-spacer"></span><span>#03-22 Singapore 519307</span></li>
      <li>
        <svg viewBox="0 0 12 12" aria-hidden="true"><path d="M2.5 0.5l2 2.5-1.2 1.3c.8 1.7 2 2.9 3.7 3.7L8.3 6.8l2.7 2-.9 2.4C5 11 1 7 .6 1.6z"/></svg>
        <span>+65 8372 6094</span>
      </li>
      <li>
        <svg viewBox="0 0 12 12" aria-hidden="true"><path d="M0 2h12v8H0zM1 3v.3l5 3.4 5-3.4V3z"/></svg>
        <span>kvlorne@mailbox47.com</span>
      </li>
    </ul>
  </section>

  <section class="card card-front" aria-label="Business card front">
    <div class="wordmark">KV Strategy Partners</div>
    <p class="tagline">Shaping enduring partnerships</p>
  </section>
</main>
</body>
</html>
```